【依頼の目的/概要】
電子書籍(pavlo)の表紙デザインをお願いします

【画像サイズ】
*RVSより抜粋
表紙ファイルの理想的な寸法は2,560×1,600ピクセルです。
注:画像の寸法は1,000×625ピクセル以上であることが必要です
画像の最大の寸法は10,000×10,000ピクセルです

【タイトル】
朝の庭で見つけた小さな灯りの話

サブキャッチ
~来場者2倍、満足度9割の老舗書店を育てた5つの習慣

【著者】
ミドリノタネ工房代表
組織進化コンサルタント
柳瀬 公平

【本の内容】
とても勤勉で勉強家の開業歯科医のみなさんが
がんばってもなかなか成果の出づらい分野、
「チーム創り」について。

まず互いを人として大事にすることで
スタッフが自然に結束し、
「ここで働けてよかった」
と思うようになる。
楽しいから自主的創造的に動くようになる。
すると成果の質も高くなる。
そうなるまでのステップを紹介。

著者はレポートを出す型のコンサルではなく、
現場に入り込んでゲーム性の高い体験型研修や
一人一人の話を聴いて言葉にならない本音を通訳することなどが得意。
愛と遊び心をもってプログラムを提供し伴走するので
笑顔が絶えることがない。

*参考資料として原稿を添付します

【デザイン要望】
特にイメージにこだわりはありませんので
自由な発想でのデザインご応募を楽しみにしています。

*次点、次々点の方への参加報酬を設定いたしました。

*その他、必要な情報がありましたらお問い合わせください。

スマホでpavloを見るとき、小さなアイコンが並ぶ中で最も目に留まるデザインで、
一目で重要なワードも目に入るデザインだったので採用させていただきました。

次点の二つについても同様の基準でしたが
色使いやフォントサイズなどを調整して、
もっとパッと目に入るものでしたら順序が変わったかもしれません。

特に、チームがテーマなので人の写真+見やすいデザインが両方だったらよりよかったかなと思います

皆さま、一所懸命やっていただいてありがとうございました。
こんなにもたくさんの方にご提案いただけてとてもうれしいです。
お礼を出せるのは3作品ですが
皆様にお礼を改めて申し上げたいと思います。

電子書籍の売れ行きにとても大事な表紙づくりのご協力、本当にありがとうございました。

```html
<!DOCTYPE html>
<html lang="ja">
<head>
<meta charset="utf-8">
<title>朝の庭で見つけた小さな灯りの話</title>
<link rel="stylesheet" href="https://fonts.googleapis.com/css2?family=M+PLUS+1p:wght@500;700;800;900&display=swap">
<style>
  :root {
    --ink: #1a1a1a;
    --blue: #1b73c9;
    --blue-deep: #1462b0;
    --blue-pale: #dcecf9;
    --white: #ffffff;
    --art-top: #f3efe6;
    --art-bottom: #e6eef6;
  }
  * { margin: 0; padding: 0; box-sizing: border-box; }
  html, body { width: 749px; height: 1200px; overflow: hidden; background: var(--white); }
  body { font-family: "M PLUS 1p", sans-serif; color: var(--ink); }
  .cover { position: relative; width: 749px; height: 1200px; background: var(--white); }

  .lead {
    position: absolute; top: 28px; left: 0; width: 100%;
    text-align: center; font-weight: 800; font-size: 34px; line-height: 1.3;
  }
  .steps {
    position: absolute; top: 108px; left: 0; width: 100%;
    text-align: center; font-weight: 900; font-size: 70px; line-height: 1.2;
  }
  .steps .num { font-size: 108px; vertical-align: -6px; margin-right: 4px; }

  .title-upper {
    position: absolute; top: 228px; left: 0; width: 100%; height: 186px;
    background: var(--blue-pale);
    border-top: 4px solid var(--blue); border-bottom: 4px solid var(--blue);
    display: flex; flex-direction: column; justify-content: center; align-items: center;
    color: var(--blue); font-weight: 900; font-size: 74px; line-height: 1.12;
  }
  .title-band {
    position: absolute; top: 432px; left: 0; width: 100%; height: 128px;
    background: var(--blue);
    border-top: 4px solid var(--blue-deep); border-bottom: 4px solid var(--blue-deep);
    display: flex; justify-content: center; align-items: center;
    color: var(--white); font-weight: 900; font-size: 100px; letter-spacing: 6px;
  }

  .team-art {
    position: absolute; top: 590px; left: 30px; width: 689px; height: 410px;
    border-radius: 12px;
    background: linear-gradient(180deg, var(--art-top), var(--art-bottom));
  }

  .author {
    position: absolute; right: 40px; top: 1010px; text-align: right;
  }
  .author .role { font-weight: 700; font-size: 22px; line-height: 1.35; }
  .author .name-line { margin-top: 10px; font-weight: 800; }
  .author .label { font-size: 30px; margin-right: 14px; }
  .author .name { font-size: 64px; letter-spacing: 4px; }
</style>
</head>
<body>
  <main class="cover">
    <p class="lead">来場者2倍、満足度9割の<br>老舗書店を育てた</p>
    <p class="steps"><span class="num">5</span>つの習慣</p>

    <h1>
      <span class="title-upper"><span>朝の庭で</span><span>見つけた小さな</span></span>
      <span class="title-band">灯りの話</span>
    </h1>

    <div class="team-art" role="img" aria-label="笑顔で並ぶ書店スタッフたちのイラスト"></div>

    <div class="author">
      <p class="role">ミドリノタネ工房代表<br>組織進化コンサルタント</p>
      <p class="name-line"><span class="label">著者</span><span class="name">柳瀬 公平</span></p>
    </div>
  </main>
</body>
</html>
```